Business Card Design

Personal training studio. My colors are burnt orange and grey. Specializing in group training and total body composition change. Nutritional consultant and contest prep.

Target Market(s)

My audience are people who are looking for total body composition change as well as knowledge on how to effectively receive results in the gym that they are a member of.

Industry/Entity Type

Training

Contact Information for Business Card

Dr. Maris Thackery
Marisjthackery@plumvane.com
3129071436
2815 west Brell ave.
Harlowmere Kestra 58214

Colors
f37122
aaaaaa

Requirements
Must have
• Animphasis on gaining knowledge that will sustain them for a life time. Healthy results and notice me results.
Nice to have
• Card should correlate with the colors of the studio. Orange and grey. With black flooring with orange speckles in it.

```html
<!DOCTYPE html>
<html lang="en">
<head>
<meta charset="utf-8">
<title>Ironvale Training Studio – Business Card</title>
<link href="https://fonts.googleapis.com/css2?family=Open+Sans:wght@400;600;700&display=swap" rel="stylesheet">
<style>
  :root {
    --burnt-orange: #f37122;
    --deep-orange: #d9480f;
    --light-orange: #f59a3c;
    --steel-grey: #aaaaaa;
    --card-black: #1c1c1c;
    --card-charcoal: #3a3a3a;
    --ink-dark: #222222;
    --text-light: #e6e6e6;
    --backdrop: #ecebe8;
  }
  html, body {
    margin: 0;
    width: 1200px;
    height: 913px;
    overflow: hidden;
    background: var(--backdrop);
    font-family: "Open Sans", Arial, sans-serif;
  }
  .canvas {
    position: relative;
    width: 1200px;
    height: 913px;
  }
  .card {
    position: absolute;
    width: 540px;
    height: 308px;
    border-radius: 4px;
    overflow: hidden;
    box-shadow: 0 10px 28px rgba(0,0,0,0.25);
  }
  .card-front {
    left: 90px;
    top: 110px;
    background: linear-gradient(135deg, var(--card-charcoal) 0%, var(--card-black) 55%, #111 100%);
  }
  .card-back {
    left: 570px;
    top: 480px;
    background: linear-gradient(135deg, #3b3b3b 0%, var(--card-black) 100%);
  }
  .brand {
    position: absolute;
    display: flex;
    align-items: center;
    gap: 14px;
  }
  .brand-dot {
    width: 46px;
    height: 46px;
    border-radius: 50%;
    background: var(--burnt-orange);
    flex: none;
  }
  .brand-name {
    font-weight: 700;
    font-size: 22px;
    line-height: 1.15;
    letter-spacing: 1px;
    text-transform: uppercase;
    white-space: nowrap;
  }
  .card-front .brand {
    left: 50%;
    top: 50%;
    transform: translate(-50%, -50%);
  }
  .card-front .brand-name { color: var(--steel-grey); }
  .card-back .orange-panel {
    position: absolute;
    inset: 0;
  }
  .card-back .brand {
    left: 34px;
    top: 50%;
    transform: translateY(-50%);
  }
  .card-back .brand-dot { background: #fff; }
  .card-back .brand-name { color: var(--ink-dark); }
  .contact {
    position: absolute;
    left: 330px;
    top: 44px;
    color: var(--text-light);
  }
  .contact-name {
    margin: 0;
    color: var(--burnt-orange);
    font-weight: 700;
    font-size: 17px;
  }
  .contact-role {
    margin: 2px 0 0;
    font-size: 11px;
  }
  .contact-list {
    list-style: none;
    margin: 46px 0 0;
    padding: 0;
    font-size: 10.5px;
    line-height: 1.6;
  }
  .contact-list li {
    display: flex;
    align-items: center;
    gap: 6px;
  }
  .contact-list svg { width: 10px; height: 10px; flex: none; }
  .address {
    margin: 12px 0 0;
    font-size: 10.5px;
    line-height: 1.5;
  }
</style>
</head>
<body>
<main class="canvas">
  <section class="card card-front" aria-label="Business card front">
    <div class="brand">
      <span class="brand-dot"></span>
      <span class="brand-name">Ironvale<br>Training<br>Studio</span>
    </div>
  </section>

  <section class="card card-back" aria-label="Business card back">
    <svg class="orange-panel" viewBox="0 0 540 308" preserveAspectRatio="none" aria-hidden="true">
      <defs>
        <linearGradient id="panelFill" x1="0" y1="0" x2="0.4" y2="1">
          <stop offset="0" stop-color="var(--light-orange)"/>
          <stop offset="0.5" stop-color="var(--burnt-orange)"/>
          <stop offset="1" stop-color="var(--deep-orange)"/>
        </linearGradient>
      </defs>
      <path d="M0 0 H240 C250 90 330 170 312 308 H0 Z" fill="var(--steel-grey)" transform="translate(8 0)"/>
      <path d="M0 0 H240 C250 90 330 170 312 308 H0 Z" fill="url(#panelFill)"/>
    </svg>
    <div class="brand">
      <span class="brand-dot"></span>
      <span class="brand-name">Ironvale<br>Training<br>Studio</span>
    </div>
    <div class="contact">
      <h1 class="contact-name">Dr. Maris Thackery</h1>
      <p class="contact-role">Personal trainer</p>
      <ul class="contact-list">
        <li>
          <svg viewBox="0 0 10 10" aria-hidden="true"><path d="M2 1 L4 1 L4.6 3 L3.5 4 C4 5.2 4.8 6 6 6.5 L7 5.4 L9 6 L9 8 C5 8.5 1.5 5 2 1 Z" fill="var(--burnt-orange)"/></svg>
          3129071436
        </li>
        <li>
          <svg viewBox="0 0 10 10" aria-hidden="true"><rect x="0.5" y="2" width="9" height="6" fill="var(--burnt-orange)"/><path d="M0.5 2 L5 5.5 L9.5 2" stroke="var(--card-black)" stroke-width="0.8" fill="none"/></svg>
          Marisjthackery@plumvane.com
        </li>
      </ul>
      <p class="address">2815 west Brell ave. Harlowmere<br>Kestra 58214</p>
    </div>
  </section>
</main>
</body>
</html>
```